Eneginering consultancy brochure style web design project

Looking for a new brochure style web page for our small engineering consultancy. The prupose of the website is to provide some basic information with about the company, including exampels of our work, and present a way to initiate contact. There there will only be a few pages (up to 5) and limited content.A main focus of the project is to develop the visual design/identity for the webpage, and to provide the template for us to add content, rearrange layout and modify pages with relative ease.A mixture of text and images will be used. The use of an image slider would be desirable.We have recently had a new company logo developed (uploaded), which defines the colour scheme for the page.A professional. clean look is desired, that is not cluttered and easy to navigate.Template to add a photo slider is desirable.The use of swirl patterns (suach as those used here: https://www.brightvortexlab.co.uk/) and/or contoured mesh pattern (example attached) within the page is likely to be attractive, as this is in harmony with our activities.

Target Market(s)

Engineering; manufacturing

Industry/Entity Type

Engineering Consultant

Coding

Coded - Design and coding required

Number of Pages Required

3 page

Font styles to use
Other font styles liked:
• Helvetica

Colors
00a990
33b8a4
86cfc6
606060
3176b5
0255a3
85acd3
474747
7f7f7f

Requirements
Must have
• 1) Landing page for information about the company. Mostly text, with image slider.
• 2) One page for example projects. Images with accompanying texts.
• 3) Enquiry/'get in touch' page.
• Simple, uncluttered look and feel.

```html
<!DOCTYPE html>
<html lang="en">
<head>
<meta charset="utf-8">
<title>Norvane – Engineering Consultancy</title>
<link href="https://fonts.googleapis.com/css2?family=Montserrat:wght@400;600;700&family=Open+Sans:ital,wght@0,400;0,600;1,400&display=swap" rel="stylesheet">
<style>
:root{
  --green:#00a990;--green-mid:#33b8a4;--mint:#86cfc6;
  --grey:#606060;--blue:#3176b5;--navy:#0255a3;--sky:#85acd3;
  --dark:#474747;--mute:#7f7f7f;--paper:#f2f2f2;--slate:#5b6776;
}
*{box-sizing:border-box;margin:0;padding:0}
html,body{width:1158px;height:1200px;overflow:hidden;background:#fff}
body{position:relative;font-family:"Open Sans",Helvetica,Arial,sans-serif;color:var(--dark)}
.abs{position:absolute}
.heading{font-family:Montserrat,Helvetica,Arial,sans-serif;font-weight:700;line-height:.95;color:#1e2a38;text-transform:uppercase}
.heading::after{content:"";display:block;width:70px;height:2px;background:#1e2a38;margin-top:2px}
.tiny{font-size:3.5px;line-height:5px;color:var(--mute)}

/* ---------- long page (left) ---------- */
.page{left:0;top:0;width:305px;height:1200px;overflow:hidden}
.nav{top:0;left:0;width:305px;height:16px;background:#fff;display:flex;align-items:center;padding:0 34px;gap:8px;font-size:3.5px;color:var(--mute)}
.nav .brand{font-family:Montserrat,sans-serif;font-weight:700;font-size:6px;color:var(--navy);margin-right:22px;display:flex;align-items:center;gap:2px}
.nav .brand i{width:5px;height:5px;background:var(--navy);display:block}
.nav .btn{margin-left:auto;border:1px solid var(--blue);padding:0 4px;border-radius:2px;color:var(--blue)}
.hero{top:16px;left:0;width:305px;height:155px;background:linear-gradient(100deg,#8fc3cf 0%,#a7cfd8 55%,#c1dde3 100%);overflow:hidden}
.hero .pattern{right:0;top:0;width:190px;height:155px;background:radial-gradient(ellipse at 70% 45%,rgba(49,118,181,.45),rgba(49,118,181,0) 65%)}
.hero .mark{left:25px;top:55px;width:70px;height:70px;background:linear-gradient(135deg,#6f9fe0,#2d62c4);transform:rotate(45deg);opacity:.8}
.hero .play{left:38px;top:66px}
.hero h1{left:72px;top:69px;font-family:"Open Sans",sans-serif;font-weight:400;font-size:10.5px;color:#fff}
.hero p{left:74px;top:84px;font-size:3.5px;color:#fff}
.services{top:171px;left:0;width:305px;height:69px;background:var(--blue)}
.services .heading{left:41px;top:24px;font-size:12px;color:#fff}
.services .heading::after{background:#fff;width:68px}
.feature{display:flex;gap:5px;width:80px;align-items:flex-start}
.feature .ic{width:18px;height:18px;border:1px solid #fff;border-radius:50%;flex:none;display:flex;align-items:center;justify-content:center}
.feature b{display:block;font-size:3px;color:#fff;font-weight:600}
.feature span{font-size:2.8px;line-height:3.6px;color:#dfe9f5;display:block}
.steps{top:240px;left:0;width:305px;height:28px;background:var(--green)}
.steps .bar{left:82px;top:13px;width:140px;height:3px;background:#d9e6ea}
.step{top:4px;width:20px;height:20px;border-radius:50%;background:#fff;border:3px solid #c5d3d8;display:flex;align-items:center;justify-content:center;font:700 9px Montserrat,sans-serif;color:var(--blue)}
.works{top:268px;left:0;width:305px;height:254px;background:#ebebeb}
.works .step-label{position:absolute;top:1px;width:36px;text-align:center;font-size:3.6px;line-height:4px;color:var(--dark)}
.works .heading{left:41px;top:18px;font-size:12px}
.tabs{left:41px;top:49px;display:flex;gap:2px}
.tabs span{font-size:3px;padding:1px 4px;border:1px solid var(--blue);color:var(--blue);background:#fff}
.tabs span.on{background:var(--blue);color:#fff}
.progress{left:124px;top:47px;width:138px;height:10px;background:#fff;border-radius:5px;display:flex;font-size:3.5px;align-items:center}
.progress .done{background:var(--blue);color:#fff;height:10px;border-radius:5px;padding:0 8px;display:flex;align-items:center}
.progress span{padding:0 7px;color:var(--blue)}
.progress span.off{color:var(--mute)}
.photo{width:70px;height:71px;background:linear-gradient(160deg,#8fb3d6,#4f6e8e)}
.photo.warm{background:linear-gradient(160deg,#d9b98e,#6e7f94)}
.photo.sky{background:linear-gradient(170deg,#6aa5e5,#2f5f9a)}
.photo.card{height:61px}
.caption{width:70px;height:15px;background:#fff;text-align:center;font-size:3px;line-height:4px;padding-top:3px;color:var(--mute)}
.caption b{color:var(--blue);display:block}
.slider{left:43px;top:235px;width:220px;height:3px;background:#cfd6dc}
.slider i{display:block;width:150px;height:3px;background:var(--blue)}
.dark-band{left:0;width:305px;background:linear-gradient(180deg,#4e5a68,#3f4a57)}
.quote{top:522px;height:65px;text-align:center;color:#dfe6ee;font-size:6px;line-height:8px;padding:10px 70px 0}
.quote .av{width:12px;height:12px;border-radius:50%;background:#c8a986;margin:3px auto 0}
.team{top:587px;left:0;width:305px;height:175px;background:#fff}
.team .pattern{right:0;top:40px;width:80px;height:135px;background:radial-gradient(ellipse at 100% 50%,rgba(49,118,181,.35),rgba(49,118,181,0) 70%)}
.team .heading{left:41px;top:18px;font-size:12px}
.member{top:62px;width:70px}
.member .ph{width:30px;height:30px;border-radius:50%;background:#c9c9c9}
.member .ph.p1{background:linear-gradient(160deg,#d8b69a,#7a6a5e)}
.member .soc{position:absolute;left:32px;top:11px;display:flex;gap:2px}
.member .soc i{width:8px;height:8px;border-radius:50%;background:var(--blue);display:block}
.member b{display:block;font-size:3.5px;color:var(--blue);margin-top:10px}
.member em{display:block;font-size:3px;color:var(--mute);font-style:normal;margin-bottom:3px}
.stats{top:762px;height:66px;display:flex;justify-content:space-around;padding:15px 40px 0;color:#e6ebf0}
.stats div{text-align:center}
.stats strong{display:block;font:400 14px "Open Sans",sans-serif;margin-top:2px}
.stats small{font-size:3px;display:block}
.skills{top:828px;left:0;width:305px;height:160px;background:#fff}
.skills .pattern{left:0;top:70px;width:305px;height:90px;background:radial-gradient(ellipse at 30% 100%,rgba(49,118,181,.3),rgba(49,118,181,0) 70%)}
.skills .heading{left:41px;top:18px;font-size:12px}
.skills .dial{top:60px}
.note{left:203px;top:20px;width:74px;height:110px;background:#d5f0e8;border:1px solid #a9d8cc;padding:6px 5px;font-size:2.8px;line-height:3.7px;color:#3d5550;overflow:hidden}
.knob{left:284px;top:18px;width:8px;height:55px;border-radius:4px;background:linear-gradient(180deg,#e0e0e0,var(--green))}
.news{top:988px;left:0;width:305px;height:15px;background:var(--green);font-size:5px;color:#e6f6f3;display:flex;align-items:center;justify-content:center;gap:30px}
.news span.btn{background:#fff;color:var(--green);font-size:3px;padding:1px 5px;border-radius:2px}
.brands{top:1003px;height:28px;display:flex;gap:8px;align-items:center;padding:0 62px}
.brands i{width:32px;height:10px;border-radius:2px;background:rgba(255,255,255,.35);display:block}
.contact{top:1031px;left:0;width:305px;height:135px;background:var(--mint)}
.contact .heading{left:41px;top:24px;font-size:12px}
.contact .addr{left:41px;top:56px;font-size:3px;line-height:4.5px;color:#3f6b66}
.contact .dots{left:41px;top:68px;display:flex;gap:4px}
.contact .dots i{width:3px;height:3px;border-radius:50%;background:#fff;display:block}
.field{background:transparent;border:1px solid #4f8f87;height:9px;font-size:3px;color:#2f5f59;padding:2px 3px}
.send{background:#fff;font-size:3.5px;color:var(--blue);display:flex;align-items:center;justify-content:center}
.footer{top:1166px;left:0;width:305px;height:34px;background:var(--blue);text-align:center;color:#fff;font-size:3px;padding-top:9px}
.footer b{font:700 6px Montserrat,sans-serif;display:block}

/* ---------- contact page (right) ---------- */
.contact-page{left:322px;top:0;width:836px;height:520px}
.touch{left:0;top:0;width:836px;height:333px;background:var(--paper)}
.touch h2{left:120px;top:34px;font:700 16px Montserrat,sans-serif;color:#222;letter-spacing:.2px}
.touch .lead{left:120px;top:58px;width:290px;font-size:9.5px;line-height:15px;color:#333}
.touch .rule{left:120px;top:100px;width:92px;height:1px;background:var(--blue)}
.touch .body{left:120px;top:129px;width:290px;font-size:8.5px;line-height:16px;color:#444}
.touch .body p+p{margin-top:17px}
.socials{left:120px;top:262px;display:flex;gap:6px}
.socials i{width:24px;height:24px;border-radius:50%;background:var(--blue);border:2px solid var(--sky);display:block}
.input{background:#fff;border:1px solid #dcdcdc;font:italic 10px "Open Sans",sans-serif;color:#777;padding:8px 7px}
.submit{left:426px;top:229px;width:82px;height:24px;border-radius:12px;background:var(--blue);color:#fff;font:700 10px Montserrat,sans-serif;display:flex;align-items:center;justify-content:center;letter-spacing:.3px}
.agencies{left:0;top:333px;width:836px;height:116px;background:var(--green)}
.agency{top:32px;width:107px;height:52px;background:#fff;border-radius:2px;display:flex;flex-direction:column;align-items:center;justify-content:center;gap:6px;font:600 9px Montserrat,sans-serif;color:#333;text-transform:uppercase}
.agency svg{height:20px}
.site-foot{left:0;top:449px;width:836px;height:71px;background:var(--blue);color:#fff}
.site-foot span{position:absolute;top:44px;font:700 12px Montserrat,sans-serif}
.site-foot .startup{left:120px;font-weight:600;font-size:11px;letter-spacing:2px}
</style>
</head>
<body>

<!-- ===== Landing page ===== -->
<section class="page abs">
  <nav class="nav abs"><span class="brand"><i></i>Norvane</span><span>Home</span><span>Services</span><span>Portfolio</span><span>About</span><span>Contact</span><span class="btn">Enquire</span></nav>

  <header class="hero abs">
    <div class="pattern abs" role="img" aria-label="Flowing dotted mesh wave pattern"></div>
    <div class="mark abs" role="img" aria-label="Blue abstract cross shapes illustration"></div>
    <svg class="play abs" width="28" height="28" viewBox="0 0 28 28"><circle cx="14" cy="14" r="12" fill="#fff" stroke="#3176b5" stroke-width="2"/><path d="M11 8l9 6-9 6z" fill="#3176b5"/></svg>
    <h1 class="abs">Your business deserves a modern website</h1>
    <p class="abs">Clean engineering design</p>
  </header>

  <section class="services abs">
    <h2 class="heading abs">Our<br>Services.</h2>
    <div class="feature abs" style="left:125px;top:10px"><div class="ic"><svg width="10" height="10" viewBox="0 0 10 10"><path d="M5 1L2 9M5 1l3 8M3 6h4" stroke="#fff" fill="none"/></svg></div><div><b>FEATURE 1</b><span>Clear structural analysis for every build project.</span></div></div>
    <div class="feature abs" style="left:208px;top:10px"><div class="ic"><svg width="10" height="10" viewBox="0 0 10 10"><path d="M2 2l6 6M8 2L2 8" stroke="#fff"/></svg></div><div><b>FEATURE 2</b><span>Site tools and plant checks done on time.</span></div></div>
    <div class="feature abs" style="left:125px;top:42px"><div class="ic"><svg width="10" height="10" viewBox="0 0 10 10"><path d="M5 1l3 4-3 4-3-4z" stroke="#fff" fill="none"/></svg></div><div><b>FEATURE 3</b><span>Fluid flow studies for process plants.</span></div></div>
    <div class="feature abs" style="left:208px;top:42px"><div class="ic"><svg width="10" height="10" viewBox="0 0 10 10"><circle cx="5" cy="5" r="3" stroke="#fff" fill="none"/><circle cx="5" cy="5" r="1" fill="#fff"/></svg></div><div><b>FEATURE 4</b><span>Mechanical design and review support.</span></div></div>
  </section>

  <section class="steps abs">
    <div class="bar abs"></div>
    <div class="step abs" style="left:78px"><svg width="8" height="8"><path d="M1 4l2 2 4-5" stroke="#606060" fill="none"/></svg></div>
    <div class="step abs" style="left:124px"><svg width="8" height="8"><path d="M1 4l2 2 4-5" stroke="#606060" fill="none"/></svg></div>
    <div class="step abs" style="left:170px">3</div>
    <div class="step abs" style="left:217px;color:#c5d3d8">4</div>
  </section>

  <section class="works abs">
    <span class="step-label" style="left:70px">Brief Review Stage</span>
    <span class="step-label" style="left:116px">Design Draft Stage</span>
    <span class="step-label" style="left:162px;color:var(--blue)">Client Check Stage</span>
    <span class="step-label" style="left:209px;color:var(--mute)">Final Sign</span>
    <h2 class="heading abs">Our<br>Works.</h2>
    <div class="tabs abs"><span class="on">All</span><span>Website</span><span>Branding</span></div>
    <div class="progress abs"><span class="done">Completed</span><span>Active</span><span class="off">Inactive</span></div>
    <div class="abs" style="left:41px;top:67px"><div class="photo card warm" role="img" aria-label="Photo: engineers reviewing plans at a table"></div><div class="caption"><b>NAME PROJECT</b>Designed by team</div></div>
    <div class="photo sky abs" style="left:117px;top:67px" role="img" aria-label="Photo: engineer in hard hat checking equipment"></div>
    <div class="photo abs" style="left:193px;top:67px" role="img" aria-label="Photo: industrial plant interior"></div>
    <div class="photo abs" style="left:41px;top:150px" role="img" aria-label="Photo: hand adjusting a machine valve"></div>
    <div class="photo sky abs" style="left:117px;top:150px" role="img" aria-label="Photo: tall industrial chimneys against sky"></div>
    <div class="photo warm abs" style="left:193px;top:150px" role="img" aria-label="Photo: team meeting on a construction site"></div>
    <div class="slider abs"><i></i></div>
  </section>

  <section class="dark-band quote abs" role="img" aria-label="Technical drawing background with client testimonial">
    Our engineers turn complex briefs into clear, safe and lasting designs for industry.
    <div class="av"></div>
  </section>

  <section class="team abs">
    <div class="pattern abs" role="img" aria-label="Dotted mesh wave pattern"></div>
    <h2 class="heading abs">Our<br>Team.</h2>
    <div class="member abs" style="left:49px"><div class="ph p1" role="img" aria-label="Team member portrait"></div><div class="soc"><i></i><i></i><i></i></div><b>DANIEL HART</b><em>CEO &amp; Founder</em><p class="tiny">Leads project delivery and client work across all our engineering sectors.</p></div>
    <div class="member abs" style="left:128px"><div class="ph" role="img" aria-label="Team member portrait placeholder"></div><div class="soc"><i></i><i></i><i></i></div><b>OWEN PRICE</b><em>Designer</em><p class="tiny">Shapes plant layouts and models for each new build and upgrade.</p></div>
    <div class="member abs" style="left:207px"><div class="ph" role="img" aria-label="Team member portrait placeholder"></div><div class="soc"><i></i><i></i><i></i></div><b>LIAM FORDYCE</b><em>Manager</em><p class="tiny">Keeps every site running to plan, budget and safety standard.</p></div>
  </section>

  <section class="dark-band stats abs" role="img" aria-label="Technical drawing background with company figures">
    <div><small>■</small><strong>2009</strong><small>PROJECTS</small></div>
    <div><small>■</small><strong>13,562</strong><small>COMMENTS</small></div>
    <div><small>■</small><strong>8,710</strong><small>COFFEE CUPS</small></div>
    <div><small>■</small><strong>715</strong><small>AWARDS</small></div>
  </section>

  <section class="skills abs">
    <div class="pattern abs" role="img" aria-label="Dotted mesh wave pattern"></div>
    <h2 class="heading abs">Our<br>Skills.</h2>
    <svg class="dial abs" style="left:40px" width="170" height="40" viewBox="0 0 170 40">
      <g fill="none" stroke="#3176b5" stroke-width="1.6">
        <path d="M18 3a17 17 0 1 1-15 9"/><path d="M60 3a17 17 0 1 1-14 8"/><path d="M102 3a17 17 0 1 1-16 12"/><path d="M144 3a17 17 0 1 1-12 5"/>
      </g>
      <g font-size="4" fill="#3176b5" text-anchor="middle" font-family="Open Sans"><text x="20" y="21">70</text><text x="62" y="21">65</text><text x="104" y="21">75</text><text x="146" y="21">90</text></g>
    </svg>
    <p class="abs" style="left:65px;top:106px;font-size:3px;color:#3176b5">SOMETHING ABOUT OUR SKILLS</p>
    <div class="note abs"><b style="color:#00a990">■ Our specialist capabilities</b><br>We bring years of practice in structural, process and mechanical design. Each study is checked by two engineers before it reaches you, so every figure is sound. We model loads, flows and heat with care, and we explain results in plain words. Our reports are short, clear and ready for your board. We work with small firms and large plants alike, on new builds and on upgrades to older sites.</div>
    <div class="knob abs"></div>
  </section>

  <div class="news abs"><span>Enter your e-mail here...</span><span class="btn">Subscribe</span></div>
  <div class="dark-band brands abs" aria-label="Partner badges"><i></i><i></i><i></i><i></i><i></i></div>

  <section class="contact abs">
    <h2 class="heading abs">Contact<br>Us.</h2>
    <p class="addr abs">14 Mill Lane, Bristol BS1 4QT<br>+44 117 000 0000 · hello@brightvortexlab.co.uk</p>
    <div class="dots abs"><i></i><i></i><i></i><i></i><i></i><i></i></div>
    <div class="field abs" style="left:41px;top:81px;width:76px">EMAIL</div>
    <div class="field abs" style="left:122px;top:81px;width:66px">NAME</div>
    <div class="field abs" style="left:41px;top:98px;width:147px;height:16px">MESSAGE</div>
    <div class="send abs" style="left:193px;top:98px;width:70px;height:16px">Send</div>
  </section>

  <footer class="footer abs"><b>Norvane</b>© 2024 Norvane. All rights reserved.</footer>
</section>

<!-- ===== Contact page ===== -->
<section class="contact-page abs">
  <div class="touch abs">
    <h2 class="abs">GET IN TOUCH</h2>
    <p class="lead abs">Sed ut perspiciatis unde omnis iste natus error sit voluptatem accusantium doloremque laudantium totam.</p>
    <div class="rule abs"></div>
    <div class="body abs">
      <p>There are many variations of passages of Lorem Ipsum available, but the majority have suffered alteration in some form, by injected humour, or randomised words which don't look even slightly believable.</p>
      <p>If you are going to use a passage of Lorem Ipsum, you need to be sure there isn't anything embarrassing hidden in the middle of text. All the Lorem Ipsum generators on the Internet tend to repeat.</p>
    </div>
    <div class="socials abs"><i></i><i></i><i></i><i></i></div>
    <div class="input abs" style="left:426px;top:68px;width:148px;height:28px">Name</div>
    <div class="input abs" style="left:578px;top:68px;width:148px;height:28px">Email Address</div>
    <div class="input abs" style="left:426px;top:104px;width:148px;height:28px">Phone</div>
    <div class="input abs" style="left:578px;top:104px;width:148px;height:28px">Subjects</div>
    <div class="input abs" style="left:426px;top:139px;width:300px;height:80px">Any Message</div>
    <div class="submit abs">SUBMIT</div>
  </div>

  <div class="agencies abs">
    <div class="agency abs" style="left:120px"><svg width="22" height="20" viewBox="0 0 22 20"><path d="M1 4h7l2 2h10v11H1z" fill="#3176b5"/></svg>New Company</div>
    <div class="agency abs" style="left:242px"><svg width="20" height="20" viewBox="0 0 20 20"><circle cx="10" cy="10" r="8.5" fill="none" stroke="#3176b5" stroke-width="2"/><path d="M10 6l3 2-1 4h-4l-1-4z" fill="#3176b5"/></svg>New Agency</div>
    <div class="agency abs" style="left:364px"><svg width="22" height="20" viewBox="0 0 22 20"><path d="M11 1l9 5v8l-9 5-9-5V6z M2 6l9 5 9-5 M11 11v8" fill="none" stroke="#3176b5" stroke-width="1.8"/></svg>My Agency</div>
    <div class="agency abs" style="left:486px"><svg width="22" height="20" viewBox="0 0 22 18"><path d="M11 1a10 10 0 0 0-10 10c0 4 3 6 6 5s2-3 4-3 4 4 8 1a10 10 0 0 0-8-13z" fill="#3176b5"/><circle cx="6" cy="8" r="1.6" fill="#fff"/><circle cx="10" cy="5" r="1.6" fill="#fff"/><circle cx="15" cy="6" r="1.6" fill="#fff"/></svg>Your Company</div>
    <div class="agency abs" style="left:608px"><svg width="16" height="20" viewBox="0 0 16 20"><path d="M2 1h12M2 19h12M3 1c0 6 10 6 10 9s-10 3-10 9M13 1c0 6-10 6-10 9s10 3 10 9" fill="none" stroke="#3176b5" stroke-width="1.8"/></svg>Nice Agency</div>
  </div>

  <footer class="site-foot abs">
    <span class="startup">STARTUP</span>
    <span style="left:408px">Useful Links</span>
    <span style="left:545px">Quick Links</span>
    <span style="left:671px">Get In Touch</span>
  </footer>
</section>

</body>
</html>
```